Cleaning/ butler service flyer design

We need a flyer that will be distributed through letter boxes for a small company based in Leamington Spa, called Tobias and Teodoro - We offer an in depth cleaning service as a one off, or regular weekly cleaning to suit the client. Tobias and Teodoro are experienced in hotel housekeeper services, and know the difference between what looks clean and what really is clean. We would like the designs to include green and blue colours. The flyer should also have a hint of humour but communicate trust and flexibility.

I the flyer to capitalise on the personality of these two Spanish guys doing a cleaning service.
- Logo: Use words – Tobias & Teodoro
o In Century Gothic Bold font
o Use a hoover to create the ‘&’ giving it the quirky logo

Tobais & Teodoro
Cleaning at your service

I like the use of the strap line “ we know the difference between what looks clean and what really is clean”

We will provide a phone number and an email address as contact details which should appear at the bottom of the flyer.

Blue and Green colours to be used

I want the flyer to convey the fact that we don’t take our selves too seriously hence the need for humour (a bit like Tobias in crooked cottages), but the Home Cleaning Service is the main service that is offered so please use images that convey ‘Homey’ feelings.

Target Market(s)

Adults aged 36 - 55, men and women who live alone and work long hours and the last thing they want to do is clean their house on a weekend. Families with kids and or pets

Industry/Entity Type

Cleaning Service

Font styles to use
Other font styles liked:
• Century Gothic

Colors
0355a3
00a88f

Requirements
Must have
• I want to place 3 testimonials to evoke the service

```html
<!DOCTYPE html>
<html lang="en">
<head>
<meta charset="utf-8">
<title>Tobias &amp; Teodoro – Cleaning at your service</title>
<link rel="stylesheet" href="https://fonts.googleapis.com/css2?family=Montserrat:wght@700&family=Fira+Sans+Condensed:ital,wght@0,600;0,700;1,600&family=Open+Sans:wght@700&display=swap">
<style>
  :root {
    --brand-blue: #1f5fd0;
    --deep-blue: #0d3aa8;
    --bar-blue: #1a62dc;
    --mint: #3ed98a;
    --lime: #8ee82a;
    --orange: #f7881f;
    --phone-orange: #f7901e;
    --ink: #1d1d1d;
    --white: #ffffff;
    --sky: #e6f8fb;
    --pale-green: #c9f2b4;
  }
  * { box-sizing: border-box; margin: 0; padding: 0; }
  html, body { width: 1200px; height: 930px; overflow: hidden; background: #fff; }
  .flyer {
    position: relative;
    width: 1200px;
    height: 930px;
    overflow: hidden;
    background: linear-gradient(100deg, var(--sky) 0%, #d8f5dd 40%, var(--pale-green) 75%, #b6ec9a 100%);
    font-family: "Fira Sans Condensed", "Arial Narrow", sans-serif;
  }
  .backdrop { position: absolute; inset: 0; }

  .brand { position: absolute; left: 55px; top: 88px; width: 700px; }
  .brand-name {
    font-family: "Montserrat", "Century Gothic", sans-serif;
    font-weight: 700;
    font-size: 57px;
    line-height: 1;
    color: var(--brand-blue);
    letter-spacing: -0.5px;
    white-space: nowrap;
  }
  .brand-tagline {
    margin-top: 12px;
    margin-left: 22px;
    font-family: "Montserrat", "Century Gothic", sans-serif;
    font-weight: 700;
    font-size: 29px;
    letter-spacing: 7px;
    color: var(--ink);
    white-space: nowrap;
  }
  .experience {
    position: absolute;
    left: 55px; top: 201px;
    width: 685px; height: 33px;
    background: var(--mint);
    color: var(--white);
    font-family: "Fira Sans Condensed", "Arial Narrow", sans-serif;
    font-weight: 700;
    font-size: 21px;
    line-height: 33px;
    padding-left: 12px;
    white-space: nowrap;
  }

  .strapline {
    position: absolute;
    left: 790px; top: 62px; width: 380px;
    color: var(--white);
    font-family: "Fira Sans Condensed", "Arial Narrow", sans-serif;
    font-style: italic;
    font-weight: 600;
    font-size: 34px;
    line-height: 1.13;
    text-align: center;
  }

  .art { position: absolute; border-radius: 20px; }
  .art-butler { left: 105px; top: 268px; width: 200px; height: 232px; background: linear-gradient(180deg, rgba(255,255,255,.55), rgba(60,60,60,.18)); }
  .art-laundry { left: 312px; top: 264px; width: 160px; height: 210px; background: linear-gradient(180deg, rgba(255,255,255,.7), rgba(80,80,80,.15)); }
  .art-walker { left: 55px; top: 680px; width: 430px; height: 112px; background: linear-gradient(90deg, rgba(20,20,20,.55), rgba(20,20,20,.7)); }

  .seal {
    position: absolute;
    left: 735px; top: 238px;
    width: 146px; height: 146px;
    border-radius: 50%;
    background: radial-gradient(circle at 40% 35%, #ffe46a, #d6a212 70%, #9b6f08);
    box-shadow: 0 3px 8px rgba(0,0,0,.3);
  }

  .testimonials {
    position: absolute;
    left: 472px; top: 325px;
    width: 693px; height: 475px;
    background: var(--orange);
    border-radius: 30px;
    box-shadow: 4px 6px 10px rgba(0,0,0,.35);
    padding: 72px 30px 0 22px;
  }
  .testimonials-heading {
    color: var(--white);
    font-weight: 700;
    font-size: 33px;
    line-height: 1;
    text-align: center;
    margin-bottom: 18px;
  }
  .quote {
    color: var(--ink);
    font-weight: 700;
    font-size: 25.5px;
    line-height: 1.21;
    margin-bottom: 20px;
  }
  .quote:nth-of-type(2) { padding-left: 20px; }
  .quote:nth-of-type(3) { padding-left: 20px; }
  .quote cite { font-style: italic; font-weight: 600; }

  .contact-bar {
    position: absolute;
    left: 0; top: 830px;
    width: 1200px; height: 100px;
    background: var(--bar-blue);
    display: flex;
    align-items: center;
    padding-left: 175px;
    gap: 18px;
  }
  .contact-label {
    font-family: "Open Sans", Arial, sans-serif;
    font-weight: 700;
    font-size: 37px;
    color: var(--white);
  }
  .contact-phone {
    display: flex; align-items: center; gap: 6px;
    font-family: "Open Sans", Arial, sans-serif;
    font-weight: 700;
    font-size: 60px;
    color: var(--phone-orange);
    letter-spacing: 1px;
  }
</style>
</head>
<body>
<div class="flyer">
  <svg class="backdrop" width="1200" height="930" viewBox="0 0 1200 930" aria-hidden="true">
    <polygon points="0,515 1200,195 1200,265 0,585" fill="var(--lime)"/>
    <polygon points="0,585 1200,265 1200,300 0,640" fill="#b7f07a" opacity=".55"/>
    <ellipse cx="1010" cy="95" rx="265" ry="160" fill="var(--mint)"/>
    <ellipse cx="1020" cy="85" rx="255" ry="145" fill="var(--deep-blue)"/>
  </svg>

  <header class="brand">
    <div class="brand-name">TOBIAS &amp; TEODORO</div>
    <div class="brand-tagline">CLEANING AT YOUR SERVICE</div>
  </header>
  <div class="experience">With Over 10 Years of Experience Within The Hotel Cleaning Industry</div>

  <p class="strapline">We know the difference between what looks clean and what really is clean!</p>

  <div class="art art-butler" role="img" aria-label="Cartoon butler striding along carrying coat hangers"></div>
  <div class="art art-laundry" role="img" aria-label="Cartoon man hurrying with an overflowing laundry basket"></div>
  <div class="art art-walker" role="img" aria-label="Silhouette of a person walking two dogs"></div>

  <div class="seal" role="img" aria-label="Satisfaction guarantee seal"></div>

  <section class="testimonials">
    <h2 class="testimonials-heading">Hear what our satisfied clients have to say:</h2>
    <p class="quote">“We really struggled to find a reliable cleaning service that was consistent week in week out, these two Spanish guys turned up and have done and continue to do a really good job – Ole!” &nbsp;-- <cite>Harriet, Fernbrook Road</cite></p>
    <p class="quote">“ I suffer from dust allergies, so I can tell when a cleaner hasn’t been thorough, I’ve been through loads and I can tell you, these guys really do clean” -- <cite>Oliver, Ashcombe</cite></p>
    <p class="quote">“They even texted me after to ask if I was happy with the service” &nbsp;-- <cite>Rupert, Millbrook Park</cite></p>
  </section>

  <footer class="contact-bar">
    <span class="contact-label">Call for details now!</span>
    <span class="contact-phone">
      <svg width="54" height="54" viewBox="0 0 54 54" aria-hidden="true">
        <circle cx="27" cy="27" r="23" fill="none" stroke="var(--phone-orange)" stroke-width="4"/>
        <path d="M19 14c2-1 4 0 5 2l2 5c0 2-1 3-2 4 1 3 3 6 6 7 1-1 2-2 4-2l4 2c2 1 2 3 1 5-2 3-5 4-8 3-8-3-14-10-15-18 0-3 1-6 3-8z" fill="var(--phone-orange)"/>
      </svg>
      0161 496 0832
    </span>
  </footer>
</div>
</body>
</html>
```